Text design/overlay needed for promotional music release cover photo

I need the following text elements added to the attached image:
Element 1: Corwin Haskell and The Kinfolk Assembly
Element 2. This all needs to be clear and prominent : Featuring: Terrence Pawlak, Oscar Brandt, Danielle Oroszco, Renata Hollsworth, Marcus "Tater" Vinson, Lorraine Quibell, Wa Nu Ri Blake Dorsey, Philip Ostrander, Eddie Pruitt, Nolan Fitch, and The Final Grooveloid
Element 3 ("WINDING CREEK" needs to pop): New single WINDING CREEK available everywhere 9/26
The final image needs to be 16:9 ratio. Colors should be black and samples from the bench in the image. Various fonts, text sizes, etc. The music is a reggae/bluegrass blend. I'm looking for art not AI. Thanks!

```html
<!DOCTYPE html>
<html lang="en">
<head>
<meta charset="utf-8">
<title>Corwin Haskell and The Kinfolk Assembly – Winding Creek</title>
<link rel="stylesheet" href="https://fonts.googleapis.com/css2?family=Sacramento&family=Montserrat:ital,wght@0,300;1,400&family=Alfa+Slab+One&family=Bebas+Neue&display=swap">
<style>
  :root {
    --ink: #000000;
    --paper: #ffffff;
    --photo-light: #c9c9c9;
    --photo-mid: #8a8a8a;
    --photo-dark: #3a3a3a;
  }
  html, body {
    margin: 0;
    padding: 0;
    width: 1200px;
    height: 675px;
    overflow: hidden;
    background: var(--ink);
  }
  .release-card {
    position: relative;
    width: 1200px;
    height: 675px;
    background: var(--ink);
    overflow: hidden;
    color: var(--paper);
  }
  .artist-photo {
    position: absolute;
    left: 0;
    top: 0;
    width: 640px;
    height: 675px;
    background:
      linear-gradient(180deg, var(--photo-dark) 0%, var(--photo-mid) 30%, var(--photo-light) 60%, var(--photo-mid) 100%);
  }
  .torn-edge {
    position: absolute;
    left: 0;
    top: 0;
    width: 1200px;
    height: 675px;
  }
  .headline {
    position: absolute;
    right: 47px;
    text-align: right;
    margin: 0;
    white-space: nowrap;
  }
  .artist-name {
    top: 62px;
    font-family: "Sacramento", cursive;
    font-weight: 400;
    font-size: 92px;
    line-height: 1;
  }
  .band-name {
    top: 172px;
    font-family: "Montserrat", sans-serif;
    font-style: italic;
    font-weight: 400;
    font-size: 30px;
  }
  .single-label {
    top: 258px;
    font-family: "Montserrat", sans-serif;
    font-weight: 300;
    font-size: 48px;
    letter-spacing: 0.5px;
  }
  .single-title {
    top: 318px;
    font-family: "Alfa Slab One", serif;
    font-size: 57px;
    line-height: 1.1;
  }
  .release-date {
    top: 394px;
    font-family: "Montserrat", sans-serif;
    font-weight: 300;
    font-size: 29px;
  }
  .featuring-label {
    top: 474px;
    font-family: "Bebas Neue", sans-serif;
    font-size: 52px;
    line-height: 1;
  }
  .featuring-list {
    position: absolute;
    right: 47px;
    top: 533px;
    width: 500px;
    margin: 0;
    text-align: right;
    font-family: "Bebas Neue", sans-serif;
    font-size: 21px;
    line-height: 31px;
    letter-spacing: 0.2px;
  }
</style>
</head>
<body>
  <main class="release-card">
    <div class="artist-photo" role="img" aria-label="Black and white photo of the musician seated on a wooden bench beside an electric guitar on a gravel country road lined with trees"></div>

    <svg class="torn-edge" viewBox="0 0 1200 675" aria-hidden="true">
      <polygon fill="#000" points="
        530,0 524,30 532,58 528,90 538,118 534,150 545,178 540,210 552,240 548,268 560,296
        556,330 566,360 562,392 574,420 570,452 582,480 578,512 590,540 586,572 598,600
        594,632 604,660 602,675 1200,675 1200,0"/>
    </svg>

    <h1 class="headline artist-name">Corwin Haskell</h1>
    <p class="headline band-name">and The Kinfolk Assembly</p>

    <p class="headline single-label">NEW SINGLE</p>
    <h2 class="headline single-title">WINDING CREEK</h2>
    <p class="headline release-date">AVAILABLE EVERYWHERE 9/26</p>

    <h3 class="headline featuring-label">FEATURING:</h3>
    <p class="featuring-list">
      TERRENCE PAWLAK, OSCAR BRANDT, DANIELLE OROSZCO, RENATA HOLLSWORTH,
      MARCUS "TATER" VINSON, LORRAINE QUIBELL, WA NU RI BLAKE DORSEY, PHILIP
      OSTRANDER, EDDIE PRUITT, NOLAN FITCH, AND THE FINAL GROOVELOID
    </p>
  </main>
</body>
</html>
```